Web Design for Harbor Ledger Allies

Harbor Ledger Allies needs the photoshop files for a simple, clean and professional website design. The company is building a network of bookkeepers/accountants to handle outsourced bookkeeping services for start ups and small businesses. It needs to both attract bookkeepers to become partners and give clients confidence in the professional network. The partners will use products like Tallymint Web, Brightfolio.example and PennyTrim.example for start ups, as well as help with tasks using the clients existing accounting software.

A home and subpage design is needed. I'll award the work based on the home design. The minor subpage changes can be worked out in the workroom stage.

The pages for the navigation will be: Home, Services, Locations, Partners, FAQ, Contact

```html
<!DOCTYPE html>
<html lang="en">
<head>
<meta charset="utf-8">
<title>Harbor Ledger Allies</title>
<link rel="stylesheet" href="https://fonts.googleapis.com/css2?family=Open+Sans:wght@400;600;700&family=Oswald:wght@500;700&display=swap">
<style>
:root{
  --green:#6cb33f;
  --orange:#f26522;
  --ink:#333;
  --muted:#888;
  --dark:#232323;
  --darker:#1a1a1a;
  --footer:#3b3b3b;
  --band:#eeeeee;
  --line:#dddddd;
  --white:#fff;
}
*{box-sizing:border-box;margin:0;padding:0}
html,body{width:681px;height:1200px;overflow:hidden}
body{font-family:"Open Sans",Arial,sans-serif;color:var(--ink);background:var(--white);font-size:7px;line-height:1.4}
.topbar{height:24px;background:var(--darker);color:#bbb;display:flex;align-items:center;justify-content:space-between;padding:0 60px;font-size:7px}
.topbar .actions span{display:inline-block;padding:3px 8px;color:var(--white);font-size:6px;font-weight:600;margin-left:4px}
.btn-green{background:var(--green)}
.btn-orange{background:var(--orange)}
.header{height:58px;display:flex;align-items:center;justify-content:space-between;padding:0 60px;border-bottom:1px solid var(--line)}
.brand{display:flex;align-items:center;gap:6px;font-weight:700;font-size:10px;color:#2e6b8a}
.brand i{width:18px;height:18px;border-radius:50%;background:#2e6b8a;display:block}
.nav{display:flex;gap:2px}
.nav a{font-size:6.5px;font-weight:600;color:#555;padding:6px 8px;text-decoration:none}
.nav a.active{background:var(--green);color:var(--white)}
.hero{position:relative;height:234px;background:linear-gradient(180deg,#3c3c3c,#151515);text-align:center;color:var(--white);overflow:hidden}
.hero .photo{position:absolute;inset:0;background:radial-gradient(ellipse at 50% 40%,#5a5a5a,#1c1c1c 75%)}
.hero .lead{position:relative;padding-top:44px;font-family:"Oswald",sans-serif;font-weight:500;font-size:11px;letter-spacing:.5px}
.hero h1{position:relative;font-family:"Oswald",sans-serif;font-weight:700;font-size:32px;line-height:1.1}
.hero .cta{position:relative;display:inline-block;margin-top:12px;background:var(--orange);font-size:6px;font-weight:700;padding:6px 14px}
.hero .server{position:relative;margin:16px auto 0;width:190px;height:62px;background:linear-gradient(180deg,#777,#2a2a2a);border-radius:2px}
.hero .arrow{position:absolute;top:110px;font-size:16px;color:#ddd}
.searchbar{height:40px;display:flex;align-items:center;gap:6px;padding:0 152px;border-bottom:1px solid var(--line)}
.searchbar label{font-size:6px;color:var(--muted)}
.searchbar .field{flex:1;height:14px;border:1px solid var(--line)}
.searchbar span{color:var(--white);font-size:6px;font-weight:700;padding:3px 8px}
.intro{height:118px;padding:10px 60px 0}
.intro h2{font-size:13px;font-weight:400;color:var(--orange);margin-bottom:8px}
.intro .row{display:flex;gap:12px}
.intro .pic{width:110px;height:76px;background:linear-gradient(160deg,#9fc7e8,#6fa15a)}
.checks{flex:1;display:grid;grid-template-columns:1fr 1fr;gap:5px 8px;padding-top:4px;list-style:none}
.checks li{font-size:6.5px;color:#555;display:flex;align-items:center;gap:4px}
.testimonial{width:150px;border:1px solid var(--line);padding:8px;font-size:6px;color:var(--muted)}
.testimonial h3{font-size:8px;color:var(--ink);margin-bottom:4px}
.testimonial cite{display:block;margin-top:6px;font-style:normal;color:var(--ink)}
.features{height:186px;background:var(--band);display:flex;justify-content:space-around;padding:26px 80px 0;text-align:center}
.feature{width:140px}
.feature svg{display:block;margin:0 auto 8px}
.feature h3{font-size:11px;font-weight:400;margin-bottom:4px}
.feature h3 b{color:var(--orange);font-weight:400}
.feature p{font-size:6px;color:var(--muted)}
.pricing{height:170px;display:flex;justify-content:center;gap:14px;padding-top:14px}
.plan{width:100px;border:1px solid var(--line);text-align:center;background:var(--white);box-shadow:0 2px 3px rgba(0,0,0,.08)}
.plan h4{background:#444;color:var(--white);font-weight:400;font-size:9px;padding:6px}
.plan.featured h4{background:var(--orange)}
.plan .price{font-size:13px;font-weight:700;padding-top:6px}
.plan .per{font-size:5.5px;color:var(--muted);padding-bottom:4px}
.plan ul{list-style:none}
.plan li{font-size:5.5px;color:#666;padding:4px 0;border-top:1px solid #eee}
.plan .order{display:inline-block;margin:6px 0 8px;background:#333;color:var(--white);font-size:5.5px;font-weight:700;padding:4px 8px}
.plan.featured .order{background:var(--orange)}
.partners{height:56px;background:var(--band);display:flex;align-items:center;justify-content:center;gap:46px}
.partners i{display:block;width:50px;height:16px;background:#b5b5b5;border-radius:2px}
.skyline{height:70px;background:linear-gradient(180deg,var(--band) 0,var(--band) 30%,#3b3b3b 100%)}
.blog{height:44px;background:var(--dark);display:flex;align-items:center;gap:10px;padding:0 60px;color:#ccc}
.blog .thumb{width:34px;height:28px;background:linear-gradient(160deg,#8fb7d8,#5a8a4a)}
.blog .text{flex:1;font-size:5.5px}
.blog .text b{color:var(--white);font-size:7px}
.blog .text em{color:var(--orange);font-style:normal}
.blog .field{width:110px;height:14px;background:var(--white);color:#999;font-size:5.5px;padding:3px 5px}
.blog .send{background:var(--orange);color:var(--white);font-size:5.5px;font-weight:700;padding:3px 7px}
.footer{height:146px;background:var(--footer);display:flex;gap:20px;padding:18px 60px 0;color:#aaa;font-size:6px}
.footer .col{flex:1}
.footer h5{color:var(--white);font-size:7.5px;font-weight:600;margin-bottom:8px}
.footer li{list-style:none;margin-bottom:5px}
.footer .social li{display:flex;align-items:center;gap:5px}
.footer .social i{width:10px;height:10px;background:#555;display:block}
.bottombar{height:16px;background:var(--darker);color:#888;font-size:5.5px;display:flex;align-items:center;justify-content:space-between;padding:0 60px}
</style>
</head>
<body>
<div class="topbar">
  <span>(555) 014 2290</span>
  <span class="actions"><span class="btn-green">Sign In</span><span class="btn-orange">Join Now</span></span>
</div>
<header class="header">
  <div class="brand"><i></i>Harbor Ledger Allies</div>
  <nav class="nav">
    <a class="active">HOME</a><a>SERVICES</a><a>LOCATIONS</a><a>PARTNERS</a><a>FAQ</a><a>CONTACT US</a>
  </nav>
</header>
<section class="hero">
  <div class="photo" role="img" aria-label="Dark server room photograph"></div>
  <p class="lead">RELIABLE AND TRUSTED HOSTING QUALITY SERVER AND</p>
  <h1>FASTEST CONNECTION</h1>
  <span class="cta">GET ALL DEVELOPER OFFERS</span>
  <div class="server" role="img" aria-label="Rack server unit"></div>
  <span class="arrow" style="left:14px">&#8249;</span>
  <span class="arrow" style="right:14px">&#8250;</span>
</section>
<div class="searchbar">
  <label>Find a partner</label><div class="field"></div>
  <span class="btn-green">SEARCH</span><span class="btn-orange">ORDER</span>
</div>
<section class="intro">
  <h2>The Easiest Accounting Software for Small Businesses</h2>
  <div class="row">
    <div class="pic" role="img" aria-label="Person working on a laptop outdoors"></div>
    <ul class="checks">
      <li><svg width="7" height="7"><circle cx="3.5" cy="3.5" r="3.5" fill="#6cb33f"/><path d="M2 3.6l1 1 2-2" stroke="#fff" fill="none"/></svg>Expert Bookkeepers</li>
      <li><svg width="7" height="7"><circle cx="3.5" cy="3.5" r="3.5" fill="#6cb33f"/><path d="M2 3.6l1 1 2-2" stroke="#fff" fill="none"/></svg>Easy Setup</li>
      <li><svg width="7" height="7"><circle cx="3.5" cy="3.5" r="3.5" fill="#6cb33f"/><path d="M2 3.6l1 1 2-2" stroke="#fff" fill="none"/></svg>Monthly Reports</li>
      <li><svg width="7" height="7"><circle cx="3.5" cy="3.5" r="3.5" fill="#6cb33f"/><path d="M2 3.6l1 1 2-2" stroke="#fff" fill="none"/></svg>Real Time Billing</li>
      <li><svg width="7" height="7"><circle cx="3.5" cy="3.5" r="3.5" fill="#6cb33f"/><path d="M2 3.6l1 1 2-2" stroke="#fff" fill="none"/></svg>Payroll Support</li>
      <li><svg width="7" height="7"><circle cx="3.5" cy="3.5" r="3.5" fill="#6cb33f"/><path d="M2 3.6l1 1 2-2" stroke="#fff" fill="none"/></svg>Secure Storage</li>
      <li><svg width="7" height="7"><circle cx="3.5" cy="3.5" r="3.5" fill="#6cb33f"/><path d="M2 3.6l1 1 2-2" stroke="#fff" fill="none"/></svg>Tax Preparation</li>
      <li><svg width="7" height="7"><circle cx="3.5" cy="3.5" r="3.5" fill="#6cb33f"/><path d="M2 3.6l1 1 2-2" stroke="#fff" fill="none"/></svg>Free Consultation</li>
    </ul>
    <blockquote class="testimonial">
      <h3>Happy Clients</h3>
      Our books have never been this tidy. The partner team answers fast and keeps every month on schedule.
      <cite>Maya Ortiz, Studio Owner</cite>
    </blockquote>
  </div>
</section>
<section class="features">
  <div class="feature">
    <svg width="44" height="50" viewBox="0 0 44 50"><polygon points="22,1 43,13 43,37 22,49 1,37 1,13" fill="#d6d6d6"/><path d="M15 33l12-12M27 21a4 4 0 1 0 3-6l-2 3-3-1 1-3" stroke="#666" stroke-width="2.5" fill="none"/></svg>
    <h3><b>System</b> Admin</h3>
    <p>Our partners watch your accounts daily, fix errors early and keep every ledger clean and ready.</p>
  </div>
  <div class="feature">
    <svg width="44" height="50" viewBox="0 0 44 50"><polygon points="22,1 43,13 43,37 22,49 1,37 1,13" fill="#d6d6d6"/><rect x="14" y="15" width="16" height="6" fill="#666"/><rect x="14" y="23" width="16" height="6" fill="#666"/><rect x="14" y="31" width="16" height="6" fill="#666"/></svg>
    <h3><b>Backups</b> &amp; Storage</h3>
    <p>Files and records are saved nightly in secure cloud storage you can reach at any time.</p>
  </div>
  <div class="feature">
    <svg width="44" height="50" viewBox="0 0 44 50"><polygon points="22,1 43,13 43,37 22,49 1,37 1,13" fill="#d6d6d6"/><circle cx="22" cy="25" r="10" stroke="#666" stroke-width="2.5" fill="none"/><path d="M22 19v6l4 3" stroke="#666" stroke-width="2.5" fill="none"/></svg>
    <h3><b>24/7</b> Live Support</h3>
    <p>Reach a real bookkeeper by phone, chat or email any hour of the day or night.</p>
  </div>
</section>
<section class="pricing">
  <div class="plan"><h4>Basic</h4><div class="price">$15.00</div><div class="per">per month</div><ul><li>Transactions</li><li>Reports</li><li>SUPPORT &amp; TIPS</li><li>Software</li></ul><span class="order">ORDER NOW</span></div>
  <div class="plan"><h4>Standard</h4><div class="price">$15.00</div><div class="per">per month</div><ul><li>Transactions</li><li>Reports</li><li>SUPPORT &amp; TIPS</li><li>Software</li></ul><span class="order">ORDER NOW</span></div>
  <div class="plan featured"><h4>Premium</h4><div class="price">$15.00</div><div class="per">per month</div><ul><li>Transactions</li><li>Reports</li><li>SUPPORT &amp; TIPS</li><li>Software</li></ul><span class="order">ORDER NOW</span></div>
  <div class="plan"><h4>Maximum</h4><div class="price">$15.00</div><div class="per">per month</div><ul><li>Transactions</li><li>Reports</li><li>SUPPORT &amp; TIPS</li><li>Software</li></ul><span class="order">ORDER NOW</span></div>
</section>
<section class="partners" aria-label="Partner badges"><i></i><i></i><i></i><i></i><i></i></section>
<div class="skyline" role="img" aria-label="City skyline silhouette"></div>
<section class="blog">
  <div class="thumb" role="img" aria-label="Blog post thumbnail photo"></div>
  <div class="text"><b>FROM OUR BLOG</b> <em>Jan 12, 2024</em><br>Welcome to our network blog with weekly tips on bookkeeping, payroll and small business growth.</div>
  <div class="field">Email address</div><span class="send">SEND</span>
</section>
<footer class="footer">
  <div class="col"><h5>Harbor Ledger Allies</h5>Outsourced bookkeeping for start ups and small businesses nationwide.</div>
  <div class="col"><h5>Help &amp; Support</h5><ul><li>FAQ</li><li>Contact Us</li><li>Live Chat</li><li>Sitemap</li></ul></div>
  <div class="col"><h5>My account</h5><ul><li>Log In</li><li>Register</li><li>Order History</li><li>Settings</li></ul></div>
  <div class="col social"><h5>Social Connection</h5><ul><li><i></i>Our Page</li><li><i></i>Updates</li><li><i></i>Photos</li><li><i></i>Videos</li></ul></div>
  <div class="col"><h5>Get in Touch</h5><ul><li>(555) 014 2290</li><li>hello@harborledger.example</li><li>120 Harbor Street, Suite 4</li><li>Portland, OR 97201</li></ul></div>
</footer>
<div class="bottombar"><span>&copy; 2024 Harbor Ledger Allies. All rights reserved.</span><span>Privacy Policy | Terms &amp; Conditions</span></div>
</body>
</html>
```